Scientific business journal infographics

We are writing a scientific article for an Academic Journal (such as the Ostrander Commerce Digest, a Business Book or the Wexley Trade Gazette). This article contains 9 infographics. We have created the graphics, and they convey the correct information and have the correct text, but they are lacking in an over-arching design and style that is clear, clean and business-like. The graphics we have created were made using a combination of Powerpoint objects and organic shapes using an AI engine. The organic shapes were deliberately made to depict the part of the process that is organic, flowing and has a level of unpredictability. As opposed to the much more rigid and linear part of the processes depicted using the Powerpoint objects.

We would like to see designs that preserve this combination of rigid process and organic process, that are clear, clean, and look well-designed and professional. These will be used in scientific business journals, and need to look like they belong there.

The designs need to have editable text, and could ideally be delivered back using a combination of images put into Powerpoint slides. We will also consider other formats, as long as we can edit them using readily available software (google cloud, MSFT 365, etc)

Font styles to use
Sans Serif

Colors

Requirements
Must have
• The sample graphics have very deliberate shapes and layouts that convey the scientific intent. Try to preserve the intent and do not reimagine the graphics or stray too far from the structure provided.

```html
<!DOCTYPE html>
<html lang="en">
<head>
<meta charset="utf-8">
<title>Organizational Strategy Cycle</title>
<link rel="stylesheet" href="https://fonts.googleapis.com/css2?family=Inter:wght@400;700&display=swap">
<style>
  :root {
    --canvas-bg: #ffffff;
    --segment-fill: #b3e7f7;
    --label-blue: #1a3fc4;
    --ink: #111111;
    --divider: #b5b5b5;
  }
  html, body {
    margin: 0;
    padding: 0;
    overflow: hidden;
    background: var(--canvas-bg);
  }
  .canvas {
    position: relative;
    width: 1200px;
    height: 675px;
    overflow: hidden;
    background: var(--canvas-bg);
    font-family: "Inter", Arial, sans-serif;
    color: var(--ink);
  }
  .cycle-graphic {
    position: absolute;
    inset: 0;
  }
  .segment { fill: var(--segment-fill); }
  .segment-label {
    font-family: "Inter", Arial, sans-serif;
    font-weight: 700;
    font-size: 15.5px;
    fill: var(--label-blue);
    text-anchor: middle;
  }
  .cycle-arc {
    fill: none;
    stroke: var(--ink);
    stroke-width: 2;
  }
  .boundary {
    stroke: var(--divider);
    stroke-width: 1;
    stroke-dasharray: 1.5 2.5;
  }
  .icon { fill: var(--ink); }
  .icon-line { fill: none; stroke: var(--ink); stroke-width: 1.6; }
  .annotation {
    position: absolute;
    margin: 0;
    transform: translateX(-50%);
    text-align: center;
    font-size: 14.2px;
    line-height: 20.5px;
    font-weight: 400;
    white-space: nowrap;
  }
  .annotation--decisions { left: 541px; top: 108px; }
  .annotation--ideas { left: 775px; top: 218px; }
  .annotation--memes { left: 834px; top: 412px; }
  .annotation--maps { left: 541px; top: 557px; }
  .annotation--stories { left: 313px; top: 444px; }
  .annotation--direction { left: 312px; top: 234px; }
</style>
</head>
<body>
<div class="canvas">
  <svg class="cycle-graphic" width="1200" height="675" viewBox="0 0 1200 675" aria-label="Six-stage cycle: Decisions, Ideas, Memes, Maps, Stories, Direction">
    <defs>
      <marker id="arrow-head" viewBox="0 0 10 10" refX="8" refY="5" markerWidth="7" markerHeight="7" orient="auto">
        <path d="M1 1 L8 5 L1 9" fill="none" stroke="#111" stroke-width="1.6"/>
      </marker>
    </defs>

    <g transform="translate(539 361)">
      <!-- ring segments -->
      <g class="segments">
        <path class="segment" d="M -30.7 -63 L -73.9 -136.2 A 155 155 0 0 1 73.9 -136.2 L 30.7 -63 Z"/>
        <path class="segment" transform="rotate(60)" d="M -30.7 -63 L -73.9 -136.2 A 155 155 0 0 1 73.9 -136.2 L 30.7 -63 Z"/>
        <path class="segment" transform="rotate(120)" d="M -30.7 -63 L -73.9 -136.2 A 155 155 0 0 1 73.9 -136.2 L 30.7 -63 Z"/>
        <path class="segment" transform="rotate(180)" d="M -30.7 -63 L -73.9 -136.2 A 155 155 0 0 1 73.9 -136.2 L 30.7 -63 Z"/>
        <path class="segment" transform="rotate(240)" d="M -30.7 -63 L -73.9 -136.2 A 155 155 0 0 1 73.9 -136.2 L 30.7 -63 Z"/>
        <path class="segment" transform="rotate(300)" d="M -30.7 -63 L -73.9 -136.2 A 155 155 0 0 1 73.9 -136.2 L 30.7 -63 Z"/>
      </g>

      <!-- dotted boundaries -->
      <g class="boundaries">
        <line class="boundary" x1="-80" y1="-138.6" x2="-99" y2="-171.5"/>
        <line class="boundary" x1="80" y1="-138.6" x2="99" y2="-171.5"/>
        <line class="boundary" x1="160" y1="0" x2="198" y2="0"/>
        <line class="boundary" x1="80" y1="138.6" x2="99" y2="171.5"/>
        <line class="boundary" x1="-80" y1="138.6" x2="-99" y2="171.5"/>
        <line class="boundary" x1="-160" y1="0" x2="-198" y2="0"/>
      </g>

      <!-- clockwise arrows -->
      <g class="cycle-arrows">
        <path class="cycle-arc" marker-end="url(#arrow-head)" d="M -83.5 -157.2 A 178 178 0 0 1 83.5 -157.2"/>
        <path class="cycle-arc" marker-end="url(#arrow-head)" d="M 94.3 -150.9 A 178 178 0 0 1 177.9 -6.2"/>
        <path class="cycle-arc" marker-end="url(#arrow-head)" d="M 177.9 6.2 A 178 178 0 0 1 94.3 150.9"/>
        <path class="cycle-arc" marker-end="url(#arrow-head)" d="M 83.5 157.2 A 178 178 0 0 1 -83.5 157.2"/>
        <path class="cycle-arc" marker-end="url(#arrow-head)" d="M -94.3 150.9 A 178 178 0 0 1 -177.9 6.2"/>
        <path class="cycle-arc" marker-end="url(#arrow-head)" d="M -177.9 -6.2 A 178 178 0 0 1 -94.3 -150.9"/>
      </g>
    </g>

    <!-- segment labels -->
    <text class="segment-label" x="534" y="237">Decisions</text>
    <text class="segment-label" x="645" y="336">Ideas</text>
    <text class="segment-label" x="632" y="441">Memes</text>
    <text class="segment-label" x="541" y="499">Maps</text>
    <text class="segment-label" x="442" y="439">Stories</text>
    <text class="segment-label" x="435" y="336">Direction</text>

    <!-- icons -->
    <g class="icon-decisions" transform="translate(539 268)">
      <circle class="icon" cx="0" cy="-8" r="4"/>
      <rect class="icon" x="-5" y="-3" width="10" height="14" rx="2"/>
      <circle class="icon" cx="-12" cy="-9" r="3"/>
      <circle class="icon" cx="12" cy="-9" r="3"/>
      <path class="icon-line" d="M-8 4 L-14 4 M-12 2 L-14 4 L-12 6 M8 4 L14 4 M12 2 L14 4 L12 6"/>
    </g>
    <g class="icon-ideas" transform="translate(633 293)">
      <circle class="icon" cx="0" cy="-13" r="3.5"/>
      <circle class="icon" cx="-9" cy="-1" r="3.5"/>
      <circle class="icon" cx="9" cy="-1" r="3.5"/>
      <path class="icon" d="M-15 10 Q-9 2 -3 10 Z M3 10 Q9 2 15 10 Z"/>
      <circle class="icon" cx="0" cy="5" r="3.5"/>
      <path class="icon" d="M-6 16 Q0 8 6 16 Z"/>
    </g>
    <g class="icon-memes" transform="translate(637 397)">
      <rect class="icon" x="-14" y="-13" width="14" height="10" rx="1.5"/>
      <path d="M-9 -11 L-4 -8 L-9 -5 Z" fill="#fff"/>
      <rect x="-2" y="-4" width="16" height="12" rx="1.5" fill="#fff" stroke="#111" stroke-width="1.6"/>
      <path class="icon-line" d="M1 0 H11 M1 3.5 H9"/>
      <circle class="icon" cx="-10" cy="5" r="3.5"/>
      <path class="icon" d="M-16 15 Q-10 7 -4 15 Z"/>
    </g>
    <g class="icon-maps" transform="translate(541 465)">
      <path class="icon" d="M-13 -2 L-5 -5 L5 -2 L13 -5 L13 10 L5 13 L-5 10 L-13 13 Z"/>
      <path d="M0 -14 a5 5 0 0 1 5 5 c0 4 -5 9 -5 9 c0 0 -5 -5 -5 -9 a5 5 0 0 1 5 -5 Z" fill="#111" stroke="#b3e7f7" stroke-width="1.5"/>
      <circle cx="0" cy="-9" r="1.8" fill="#b3e7f7"/>
    </g>
    <g class="icon-stories" transform="translate(442 401)">
      <rect class="icon" x="3" y="-15" width="12" height="8" rx="4"/>
      <circle class="icon" cx="0" cy="-2" r="3.5"/>
      <circle class="icon" cx="-11" cy="3" r="3"/>
      <circle class="icon" cx="11" cy="3" r="3"/>
      <path class="icon" d="M-6 12 Q0 3 6 12 Z M-17 14 Q-11 6 -5 14 Z M5 14 Q11 6 17 14 Z"/>
    </g>
    <g class="icon-direction" transform="translate(435 297)">
      <rect class="icon" x="-13" y="-16" width="2.5" height="30"/>
      <path class="icon" d="M-10 -14 H0 L3 -11 L0 -8 H-10 Z M-10 -5 H-3 L-6 -2 L-3 1 H-10 Z" transform="translate(-4 0)"/>
      <circle class="icon" cx="9" cy="-13" r="3.5"/>
      <rect class="icon" x="4" y="-8" width="10" height="20" rx="2"/>
      <rect class="icon" x="-4" y="6" width="7" height="6" rx="1"/>
    </g>
  </svg>

  <p class="annotation annotation--decisions">Execution of critical<br>decision-making<br>processes.</p>
  <p class="annotation annotation--ideas">Conceptualization<br>of individual ideas<br>and micro<br>strategies.</p>
  <p class="annotation annotation--memes">Integration into organizational<br>lexicon and behavioural patterns,<br>incl. social cues signalling the do’s<br>and don’ts of what is deemed as<br>“acceptable” or “normal” behaviour</p>
  <p class="annotation annotation--maps">Development of<br>future state roadmaps.</p>
  <p class="annotation annotation--stories">Creation<br>of coherent and<br>adaptable narratives.</p>
  <p class="annotation annotation--direction">Provision of<br>guidance and<br>directives.</p>
</div>
</body>
</html>
```